Professional Website Design to match new logo for Medical Legal Company

We have rebranded our company and We want a professional but also dynamic web site design for a group of esteemed doctors that provide expert evaluation of an injured worker in a Workers Compensation case.
​
1. Our target market is both the attorneys who select our doctors and any doctors who would wish to join our group.

2. Notes for the Landing Page:
- We prefer a simpler, sleeker more modern look for the landing page.
- We want a simplified landing page with one image, three buttons highlighted in Content document.
- We want the main image to be black and white but it can be splashed with color.
-We think the landing page might be enhanced by add a dark blue or black as a primary color. Of course please feel free to try any color combination you think might work.
- We want "The Meridale Circle" in large letters and "Stewards of a fair and prompt outcome" in small lettering. We don't want icons on the buttons.
- Do not want more than the one picture at top of landing page.
- We do not want any pictures that include faces. Please eliminate or replace. They will not be chosen.
- For the landing page, instead of a second set of photos please experiment with using medical symbols and legal symbols.
​
3. New Company Name: The Meridale Circle
New logo is uploaded bronze and grey/silver will be colors although we are still tweaking the colors for more metallic feel. Want simple not busy.

4. The overall Web page design needs to have some website design effect (e,g image rollover, scrolling effect, hover effect etc).

5. Please follow the attached word document file for the page content of the 4 web pages. Do not mix it up.

Previous company website: www.clinicjuristpanel.example (we wish to convert some of the content from this website to the new brand). Competitor website that we like: www.docboardly.example

Target Market(s)

Professional Elite. Attorneys and Doctors

Industry/Entity Type

Medical Legal

Coding

Coded - Design and coding required

Number of Pages Required

5+ page

Font styles to use
Other font styles liked:
• Helvetica or maybe font that matches logo. We are open

Colors

Designer to choose colors to be used in the design.

Requirements
Must have
• I can't locate on color scale but we want Bronze and Silver/Grey from logo. Additional colors can be added. Various shades of grey
Nice to have
• Black and white photos, simple elegant design
Should not have
• Images with faces of unknown people

```html
<!DOCTYPE html>
<html lang="en">
<head>
<meta charset="utf-8">
<title>The Meridale Circle</title>
<link rel="stylesheet" href="https://fonts.googleapis.com/css2?family=Inter:wght@400;500;600&family=Playfair+Display:wght@400;600;700&display=swap">
<style>
:root{
  --black:#000;
  --ink:#0b0b0c;
  --footer:#1c1c1e;
  --card-top:#38383c;
  --card-bottom:#1e1e21;
  --bronze:#b97a50;
  --bronze-light:#c98a5c;
  --bronze-dark:#5a3520;
  --silver:#c9c9c9;
  --grey:#a6a6a6;
  --white:#ffffff;
  --panel:#2a2a2d;
}
*{box-sizing:border-box;margin:0;padding:0}
html,body{width:999px;height:1200px;overflow:hidden;background:var(--black)}
body{position:relative;font-family:"Inter",Helvetica,Arial,sans-serif;color:var(--white)}
.abs{position:absolute}

.hero-image{left:0;top:0;width:999px;height:476px;
  background:radial-gradient(ellipse at 72% 40%,#6a6a6a 0%,#3c3c3c 30%,#161616 62%,#050505 100%);
  border-bottom-left-radius:60% 40px;border-bottom-right-radius:0}
.hero-shade{left:0;top:0;width:999px;height:476px;background:linear-gradient(90deg,rgba(0,0,0,.55),rgba(0,0,0,.1) 70%,rgba(0,0,0,.3))}

.site-header{left:0;top:0;width:999px;height:80px;border-bottom:1px solid var(--bronze)}
.brand{left:92px;top:20px;display:flex;align-items:center;gap:8px}
.brand-mark{width:16px;height:16px;border:2px solid var(--bronze);border-radius:50%}
.brand-name{font-family:"Playfair Display",Georgia,serif;font-weight:600;font-size:22px;color:var(--silver);letter-spacing:.5px}
.main-nav{top:39px;left:608px;display:flex;gap:31px}
.main-nav a{color:var(--silver);text-decoration:none;font-size:11.5px;font-weight:500;letter-spacing:.2px;transition:color .2s}
.main-nav a:hover{color:var(--bronze-light)}

.hero-title{left:0;width:999px;top:214px;text-align:center;font-family:"Playfair Display",Georgia,serif;font-weight:700;font-size:52px;letter-spacing:-.5px}
.hero-tagline{left:0;width:999px;top:287px;text-align:center;font-size:17px;font-weight:400}

.glow{left:80px;top:470px;width:840px;height:160px;background:radial-gradient(ellipse at 50% 35%,rgba(185,122,80,.45),rgba(185,122,80,.12) 55%,transparent 75%)}
.audience-card{top:424px;width:265px;height:131px;border:2px solid var(--bronze);border-radius:12px;
  background:linear-gradient(180deg,var(--card-top),var(--card-bottom));box-shadow:0 8px 22px rgba(185,122,80,.35);
  display:flex;flex-direction:column;align-items:center;justify-content:center;text-align:center;transition:transform .25s}
.audience-card:hover{transform:translateY(-4px)}
.audience-card.featured{background:linear-gradient(180deg,#b87a50,#8a5432 55%,#3a2416);border-color:#6e4428;top:422px}
.card-title{font-family:"Playfair Display",Georgia,serif;font-size:23px;font-weight:400;line-height:30px}
.card-note{font-size:11px;margin-top:6px}
.btn{display:inline-block;background:var(--bronze);color:var(--white);border-radius:11px;font-size:10px;font-weight:500;
  height:20px;line-height:20px;padding:0 15px;text-decoration:none;transition:background .2s}
.btn:hover{background:var(--bronze-light)}
.audience-card .btn{margin-top:12px}

.intro{left:170px;width:659px;top:638px;text-align:center;font-size:17px;line-height:20px;color:var(--grey);font-weight:400}
.intro strong{color:#d4d4d4;font-weight:500}

.newsletter{left:90px;top:766px;width:818px;height:140px;border-radius:17px;overflow:hidden;
  background:linear-gradient(90deg,#2d2d30,#28282b 55%,#323235)}
.newsletter h2{position:absolute;left:51px;top:52px;font-size:25px;font-weight:500}
.newsletter .btn{position:absolute;left:624px;top:53px;height:28px;line-height:28px;border-radius:9px;font-size:10px;padding:0 22px 0 30px;display:flex;align-items:center;gap:9px}

.footer-rule{left:80px;top:984px;width:838px;height:2px;background:linear-gradient(90deg,var(--bronze),var(--bronze-dark))}
.site-footer{left:0;top:988px;width:999px;height:212px;background:var(--footer)}
.footer-brand{left:71px;top:1030px}
.copyright{left:71px;top:1145px;font-family:"Playfair Display",Georgia,serif;font-size:8px;color:var(--grey)}
.divider{width:1px;background:var(--bronze)}
.divider-accent{left:527px;top:1076px;width:3px;height:32px;background:var(--bronze)}
.footer-heading{font-family:"Playfair Display",Georgia,serif;font-size:14px;color:var(--bronze);font-weight:400}
.footer-text{font-size:11.5px;line-height:13.2px;color:var(--silver)}
.quicklinks a{display:block;color:var(--silver);text-decoration:none;font-size:11px;font-weight:600;margin-bottom:13px}
.quicklinks a:hover{color:var(--bronze-light)}
.social{display:flex;gap:11px}
.social span{width:17px;height:17px;border-radius:50%;background:var(--bronze)}
</style>
</head>
<body>
  <div class="abs hero-image" role="img" aria-label="Black and white photograph of a judge's gavel resting beside a stethoscope"></div>
  <div class="abs hero-shade"></div>

  <header class="abs site-header">
    <div class="abs brand"><span class="brand-mark"></span><span class="brand-name">Meridale Circle</span></div>
    <nav class="abs main-nav">
      <a href="#">PHYSICIANS</a>
      <a href="#">STAKEHOLDER</a>
      <a href="#">MERIDALE GIVES</a>
    </nav>
  </header>

  <h1 class="abs hero-title">THE MERIDALE CIRCLE</h1>
  <p class="abs hero-tagline">Stewards of a fair and prompt outcome</p>

  <div class="abs glow"></div>
  <section class="abs audience-card" style="left:95px">
    <h3 class="card-title">STAKEHOLDERS</h3>
    <p class="card-note">Attorneys, Carriers, Injured Workers</p>
    <a class="btn" href="#">LEARN MORE</a>
  </section>
  <section class="abs audience-card featured" style="left:374px">
    <h3 class="card-title">QME PHYSICIANS</h3>
    <a class="btn" href="#" style="margin-top:20px">LEARN MORE</a>
  </section>
  <section class="abs audience-card" style="left:654px">
    <h3 class="card-title">MEMBER<br>PHYSICIANS</h3>
    <a class="btn" href="#">LEARN MORE</a>
  </section>

  <p class="abs intro"><strong>The Meridale Circle</strong> is a leader in Qualified Medical Evaluations and SIBTF cases in the State of California. Our doctors are dedicated to facilitating settlements through rapid, objective and well researched Expert Medical Opinions</p>

  <section class="abs newsletter">
    <div class="abs" role="img" aria-label="Soft dark hexagon texture" style="left:400px;top:0;width:418px;height:140px;background:radial-gradient(ellipse at 70% 50%,#3a3a3d,transparent 70%)"></div>
    <h2>Most Recent Newsletter</h2>
    <a class="btn" href="#">DOWNLOAD
      <svg width="13" height="13" viewBox="0 0 24 24" fill="none" stroke="#fff" stroke-width="2.2" stroke-linecap="round" stroke-linejoin="round"><path d="M12 3v12M7 10l5 5 5-5M4 17v3h16v-3"/></svg>
    </a>
  </section>

  <div class="abs footer-rule"></div>
  <footer class="abs site-footer"></footer>
  <div class="abs brand footer-brand" style="top:1030px"><span class="brand-mark"></span><span class="brand-name">Meridale Circle</span></div>
  <p class="abs copyright">© 2024 Clinic Jurist Panel</p>

  <div class="abs divider" style="left:276px;top:1022px;height:129px"></div>
  <div class="abs divider" style="left:528px;top:1028px;height:129px"></div>
  <div class="abs divider-accent"></div>
  <div class="abs divider" style="left:735px;top:1018px;height:129px"></div>

  <h4 class="abs footer-heading" style="left:325px;top:1020px">COMPANY INFO</h4>
  <p class="abs footer-text" style="left:330px;top:1057px">HEADQUARTERS<br>2280 Fernhollow Ave.<br>4th Floor<br>Brenmoor, CA 90417</p>
  <p class="abs footer-text" style="left:330px;top:1132px">Call toll free (800) 555-0142<br>Fax (310) 555-0188</p>

  <h4 class="abs footer-heading" style="left:570px;top:1026px">QUICKLINKS</h4>
  <nav class="abs quicklinks" style="left:574px;top:1060px">
    <a href="#">PHYSICIANS</a>
    <a href="#">STAKEHOLDER</a>
    <a href="#">MERIDALE GIVES</a>
  </nav>

  <h4 class="abs footer-heading" style="left:781px;top:1023px">CONNECT WITH US</h4>
  <div class="abs social" style="left:782px;top:1054px"><span></span><span></span><span></span></div>
</body>
</html>
```